Corvenne Jewelers Business Cards

A creative, cool edgy business card for our entire team that says we are a young, hip, luxury jewelry store specializing in diamonds and engagement rings but that we are also personal shoppers and trusted advisors. Our colors are Navy Blue & Platinum

I have included our past business card.

Font styles to use
Serif

Colors
0255a3

Requirements
Nice to have
• A card stock that you can write on with a pen

```html
<!DOCTYPE html>
<html lang="en">
<head>
<meta charset="utf-8">
<title>Corvenne Jewelers Business Cards</title>
<link rel="stylesheet" href="https://fonts.googleapis.com/css2?family=PT+Serif:wght@400&display=swap">
<style>
  :root {
    --navy: #0255a3;
    --platinum: #dfe7f2;
    --paper: #f4f4f4;
    --ink: #222426;
    --backdrop: #d9d9d9;
  }
  * { margin: 0; padding: 0; box-sizing: border-box; }
  html, body {
    width: 1200px; height: 1021px; overflow: hidden;
    background: var(--backdrop);
    font-family: "PT Serif", Georgia, serif;
  }
  .sheet {
    display: flex; justify-content: center; align-items: center;
    gap: 100px; width: 1200px; height: 1021px;
  }
  .card {
    position: relative; width: 400px; height: 700px; overflow: hidden;
    box-shadow: 0 6px 18px rgba(0,0,0,.18);
  }
  .card--front { background: var(--paper); }
  .card--back {
    background: var(--navy);
    display: flex; flex-direction: column; align-items: center; justify-content: center;
    gap: 26px;
  }
  .front-mark {
    position: absolute; left: 44px; top: 56px;
    display: flex; flex-direction: column; align-items: flex-start; gap: 26px;
  }
  .front-mark__ring {
    width: 250px; height: 250px; border-radius: 50%;
    border: 18px solid var(--navy);
  }
  .front-mark__name { color: var(--navy); font-size: 26px; letter-spacing: 1px; }
  .brand-dot {
    width: 70px; height: 70px; border-radius: 50%;
    border: 4px solid var(--platinum);
  }
  .brand-name { color: var(--platinum); font-size: 30px; letter-spacing: 1px; }
  .person { position: absolute; left: 44px; top: 452px; }
  .person__name { color: var(--navy); font-size: 30px; line-height: 1.1; }
  .person__role { color: var(--ink); font-size: 17px; margin-top: 2px; }
  .contacts {
    position: absolute; left: 44px; top: 560px; list-style: none;
    color: var(--ink); font-size: 19px; line-height: 1.45;
  }
  .contacts li { display: flex; align-items: center; gap: 8px; }
  .contacts svg { width: 15px; height: 15px; flex: none; }
</style>
</head>
<body>
<main class="sheet">
  <section class="card card--front">
    <div class="front-mark">
      <span class="front-mark__ring" aria-hidden="true"></span>
      <p class="front-mark__name">Corvenne Jewelers</p>
    </div>
    <div class="person">
      <p class="person__name">Maren L Whitfield</p>
      <p class="person__role">Partner</p>
    </div>
    <ul class="contacts">
      <li>
        <svg viewBox="0 0 16 16" aria-hidden="true"><path d="M3 1l3 3-1.5 2a8 8 0 0 0 5.5 5.5L12 10l3 3-2 2C7 15 1 9 1 3z" fill="#0255a3"/></svg>
        (860) 555-0147
      </li>
      <li>
        <svg viewBox="0 0 16 16" aria-hidden="true"><rect x="4" y="1" width="8" height="14" rx="1.5" fill="none" stroke="#0255a3" stroke-width="1.6"/><circle cx="8" cy="12.5" r="1" fill="#0255a3"/></svg>
        (860) 555-0192
      </li>
      <li>
        <svg viewBox="0 0 16 16" aria-hidden="true"><rect x="1" y="3" width="14" height="10" fill="none" stroke="#0255a3" stroke-width="1.6"/><path d="M1 3l7 6 7-6M1 13l5-5M15 13l-5-5" fill="none" stroke="#0255a3" stroke-width="1.4"/></svg>
        maren@corvennejewelers.com
      </li>
      <li>
        <svg viewBox="0 0 16 16" aria-hidden="true"><circle cx="8" cy="8" r="7" fill="none" stroke="#0255a3" stroke-width="1.5"/><ellipse cx="8" cy="8" rx="3" ry="7" fill="none" stroke="#0255a3" stroke-width="1.2"/><path d="M1 8h14" stroke="#0255a3" stroke-width="1.2"/></svg>
        corvennejewelers.com
      </li>
    </ul>
  </section>

  <section class="card card--back">
    <span class="brand-dot" aria-hidden="true"></span>
    <p class="brand-name">Corvenne Jewelers</p>
  </section>
</main>
</body>
</html>
```